バックとタイトルにひと工夫があるとうれしいです。コピー等は入れてもらってかまいません。
添付するイラレデータCS2に全ての内容をいれます。ただし上部の大きな写真2点は本日撮り直しますので明日にでも追加でアップします。
• 高解像度JPG (.jpg)
• イラストレーター形式 (.ai)
原稿内容が一部変更になり、撮影した写真を入れておきます。はじめに添付したファイルと差し替えてください。
貼ってある写真は解像度を落としてありますので決定時に高解像度と入れ替えていただきます。
すみません。原稿1点追加になりました。

4,200円以上の宴会料理&15名様以上でいも又は麦焼酎(4合)をサービス!!
※期間 平成24年1月末日まで ※月・水・木曜日のみ

上記2行と焼酎の写真を入れてください。よろしく御願いします。

とても賑やかで、なお和のイメージが良く出ていてとても気に入りました。文字が読みづらいところが少々ありましたが訂正して頂くより自分で直した方が早いと手を加えさせていただきました。全体的なイメージはとても良かったです。

良いデザインを作成していただきありがとうございます。また依頼することがありますのでよろしくお願いします。

```html
<!DOCTYPE html>
<html lang="ja">
<head>
<meta charset="utf-8">
<title>忘年会・新年会 ご予約承り中</title>
<link rel="stylesheet" href="https://fonts.googleapis.com/css2?family=Noto+Serif+JP:wght@400;700;900&family=Yuji+Boku&family=Noto+Sans+JP:wght@400;700;900&display=swap">
<style>
:root{
  --red:#c4161c;
  --deep-red:#7d0a0e;
  --band:#8e1016;
  --gold:#e8c66a;
  --ink:#2a1a12;
  --paper:#fbf7ee;
  --cream:#f3ead6;
  --blue:#2a4f8f;
  --photo-warm:#b98a5a;
  --photo-dark:#4a3325;
}
*{margin:0;padding:0;box-sizing:border-box}
html,body{width:849px;height:1200px;overflow:hidden}
body{background:var(--paper);font-family:"Noto Serif JP",serif;color:var(--ink);position:relative}
.abs{position:absolute}
.photo{position:absolute;background:linear-gradient(135deg,var(--photo-warm),var(--photo-dark));border-radius:2px}
.intro{left:28px;top:12px;font-size:12px;line-height:1.6}
.menu-title{left:28px;top:48px;font-size:40px;font-weight:900;letter-spacing:2px;line-height:1.2}
.badge{display:inline-block;background:var(--red);color:#fff;font-family:"Noto Sans JP",sans-serif;font-weight:700;font-size:12px;line-height:1.2;padding:4px 6px;border-radius:4px;text-align:center;vertical-align:middle;letter-spacing:0}
.price{color:var(--red);font-weight:900;font-family:"Noto Sans JP",sans-serif;line-height:1.1}
.price small{font-size:.45em}
.price-banquet{left:28px;top:104px;font-size:42px}
.drink-title{left:28px;top:162px;font-size:34px;font-weight:900;line-height:1.2}
.drink-title .limit{font-size:12px;display:inline-block;width:34px;line-height:1.2;vertical-align:middle;font-weight:700}
.price-drink{left:28px;top:212px;font-size:26px}
.drink-list{left:28px;top:252px;font-size:12px;line-height:1.7;width:280px}
.price-course{left:596px;top:448px;font-size:38px;color:var(--ink)}
.price-course small{font-size:14px}
.snow{left:596px;top:330px;font-size:44px;color:#b8b0a2;font-family:"Yuji Boku",serif}
.band{left:0;top:490px;width:849px;height:200px;background:radial-gradient(ellipse at center,#a3161c 0%,var(--band) 55%,var(--deep-red) 100%);border-top:4px solid var(--gold);border-bottom:4px solid var(--gold)}
.band .reserve{position:absolute;left:130px;top:8px;color:var(--gold);font-family:"Yuji Boku",serif;font-size:24px;transform:rotate(-6deg)}
.band .title{position:absolute;left:0;width:100%;top:46px;text-align:center;font-family:"Yuji Boku",serif;font-size:96px;color:#fff;line-height:1.1;white-space:nowrap}
.aya{left:390px;top:1000px;font-size:40px;color:#e6dccb;font-family:"Yuji Boku",serif;z-index:2}
.winter-plan{left:14px;top:704px;width:100px;height:280px;color:var(--red);font-weight:900;writing-mode:vertical-rl;font-size:34px;line-height:1.1}
.winter-plan .big{font-size:80px}
.ladies-box{left:118px;top:704px;width:318px;height:150px;border:2px solid var(--red);background:#fff;padding:10px}
.ladies-box p{font-size:13px}
.ladies-box .name{margin-top:6px;background:var(--red);color:#fff;font-weight:700;font-size:18px;padding:2px 8px;display:inline-block}
.ladies-box .period{position:absolute;right:-2px;top:-2px;width:100px;height:90px;background:var(--blue);color:#fff;font-size:13px;font-weight:700;text-align:center;padding-top:10px;line-height:1.5}
.ladies-box .lp{margin-top:8px;font-size:38px}
.ladies-detail{left:118px;top:866px;width:318px;font-size:13px;line-height:1.6}
.ladies-detail h3{color:var(--red);font-size:17px}
.ladies-detail table{border-collapse:collapse;width:100%}
.ladies-detail td{border-bottom:1px dotted #a08a70;padding:1px 4px}
.ladies-detail td.r{text-align:right;color:var(--red);font-weight:700}
.shochu{left:456px;top:704px;width:380px;height:150px;background:#fff;border:1px solid #d9c9a6;padding:10px 12px}
.shochu p{font-size:17px;font-weight:700;line-height:1.5;width:270px}
.shochu .em{color:var(--red)}
.shochu .note{position:absolute;left:10px;bottom:10px;width:270px;background:var(--blue);color:#fff;font-size:12px;padding:3px 6px}
.nabe{left:456px;top:866px;width:380px;height:200px}
.nabe h2{font-size:44px;font-weight:900;line-height:1.1}
.nabe .lead{position:absolute;left:150px;top:4px;background:var(--red);color:#fff;font-size:13px;font-weight:700;padding:4px 8px;line-height:1.4}
.nabe ul{list-style:none;font-size:13px;line-height:1.6;position:absolute;left:0;top:118px;width:200px}
.nabe .p1{position:absolute;left:0;top:78px;font-size:32px}
.nabe .p2{position:absolute;left:210px;top:162px;font-size:32px}
.osechi{left:456px;top:1080px;width:380px;height:108px;border:2px solid var(--red);background:var(--cream);padding:8px 10px}
.osechi h3{font-size:22px;color:var(--red);font-weight:900}
.osechi p{font-size:15px;line-height:1.6}
.osechi p b{color:var(--red);font-size:22px;font-family:"Noto Sans JP",sans-serif}
</style>
</head>
<body>
  <div class="abs intro">日ごろの疲れを癒して楽しいひとときを。<br>皆様のお集まりを心よりお待ちしております。</div>
  <div class="abs menu-title">宴会料理 <span class="badge">要予約<br>2名様より</span></div>
  <div class="abs price price-banquet">3,675<small>円より</small></div>
  <div class="abs drink-title"><span class="limit">2時間まで</span>飲み放題 <span class="badge">要予約<br>8名様より</span></div>
  <div class="abs price price-drink">宴会料理＋1,575<small>円</small></div>
  <div class="abs drink-list">●酒 ●ビール ●焼酎(麦・いも) ●ウーロン茶<br>●ジュース ●オリジナル果実酒</div>

  <div class="photo" style="left:320px;top:0;width:529px;height:300px" role="img" aria-label="宴会料理の盛り合わせ写真"></div>
  <div class="photo" style="left:20px;top:312px;width:560px;height:166px" role="img" aria-label="宴会料理のお膳の写真"></div>
  <div class="abs snow">雪</div>
  <div class="abs price price-course">4,200<small>円(税込)</small></div>

  <div class="abs band" role="group" aria-label="タイトル">
    <div class="reserve">ご予約承り中</div>
    <div class="title">忘年会・新年会</div>
  </div>

  <div class="abs winter-plan"><span class="big">冬</span>の特別企画</div>
  <div class="abs ladies-box">
    <p>日ごろのご来店に感謝して…</p>
    <div class="name">レディースお昼膳[綾]</div>
    <div class="price lp">1,575<small>円(税込)</small></div>
    <div class="period">期間<br>11月1日(木)<br>〜16日(金)<br>平日限定</div>
  </div>
  <div class="abs ladies-detail">
    <h3>冬のレディースお昼膳 <small>(土・祝・休日除く)</small></h3>
    <table>
      <tr><td>11月1日(木)〜16日(金)</td><td class="r">1,575円</td></tr>
      <tr><td>小鉢・お造り・天ぷら</td><td class="r">1,890円</td></tr>
      <tr><td>茶碗蒸し・ご飯・デザート</td><td class="r">2,940円</td></tr>
    </table>
  </div>
  <div class="photo" style="left:20px;top:990px;width:416px;height:200px" role="img" aria-label="レディースお昼膳の料理写真"></div>
  <div class="abs aya">綾</div>

  <div class="abs shochu">
    <p>4,200円以上の宴会料理＆<br>15名様以上で<span class="em">いも又は麦焼酎(4合)</span>をサービス!!</p>
    <div class="note">平成24年1月末日まで ※月・水・木曜日のみ</div>
    <div class="photo" style="right:12px;top:10px;width:70px;height:128px" role="img" aria-label="焼酎の瓶の写真"></div>
  </div>

  <div class="abs nabe">
    <h2>鍋もの</h2>
    <div class="lead">冬コースは全て<br>料金の内訳を選べます</div>
    <div class="price p1">5,250<small>円(税込)</small></div>
    <ul>
      <li>●ふぐちり ●すっぽん鍋</li>
      <li>●あんこう鍋 ●鴨鍋</li>
      <li>●しゃぶしゃぶ(和牛)</li>
      <li>●すき焼き(和牛)</li>
    </ul>
    <div class="price p2">4,200<small>円(税込)</small></div>
    <div class="photo" style="left:210px;top:62px;width:170px;height:92px" role="img" aria-label="鍋料理の写真"></div>
  </div>

  <div class="abs osechi">
    <h3>おせち料理</h3>
    <p>●お重 三段 <b>21,000円</b>(税込)<br>●お重 二段 <b>15,750円</b>(税込)</p>
    <div class="photo" style="right:8px;top:8px;width:130px;height:88px" role="img" aria-label="おせち料理の重箱の写真"></div>
  </div>
</body>
</html>
```